Community Harvest Festival Poster

Seeking a poster design to advertise our community’s annual Harvest Festival. We will utilize and display printed posters as well as distribute PDFs via our weekly e-news letters. This years "theme" is, "Brass Lantern/Pebble Lane Grove, Where Maple and Wren Unite." The vibe is a bohemian, beatnik, street scene, meets a old fashioned orchard.

Target Market(s)

NYC School Community- should appeal to an audience that ranges from kids to grandparents. Very family oriented, with wide appeal, and must be eye catching.

Font styles to use
Other font styles liked:
• One style should be more of a "Country" font, the other should have more of a clean city vibe.

Colors
acd037
ffc214
f68e4e
eaf2ce

Requirements
Must have
• The following copy:
• Brass Lantern Pebble Lane Grove
• Where Maple and Wren Unite
• Celebrate M&W With Great Food, Music, Entertainment, And Fun!
• Saturday, October 19th 2019
• 12:00-4:00pm
• Tickets will be available for sale at Drop off and Pick up
Nice to have
• I'm not limited, but a couple of ideas that could be cool:
• One incorporated the background of a street, i.e. pavement, which has leaves blowing over it, and perhaps an apple or two rolling onto the page.
• Another has a diagonal breakup of the image, with one side pavement and the other side rustic wood, also with leaves sweeping across.
• I've also attached images of previous festival posters that I have gravitated to for some idea of quality I'm looking for.
Should not have
• Anything inappropriate for children.

```html
<!DOCTYPE html>
<html lang="en">
<head>
<meta charset="utf-8">
<title>Brass Lantern Pebble Lane Grove – Harvest Festival</title>
<link rel="stylesheet" href="https://fonts.googleapis.com/css2?family=Rye&family=Montserrat:wght@500;600;700&family=Raleway:wght@500;700&display=swap">
<style>
  :root {
    --orange: #f68e4e;
    --cream: #eaf2ce;
    --panel: rgba(238, 241, 205, 0.86);
    --ink: #141414;
    --leaf-gold: #d9a441;
    --leaf-green: #9fb55a;
    --path-grey: #9aa39a;
    --hay: #a9773d;
  }
  * { margin: 0; padding: 0; box-sizing: border-box; }
  html, body {
    width: 1048px;
    height: 1200px;
    overflow: hidden;
    background: #f2f0ec;
  }
  .poster {
    position: relative;
    width: 1048px;
    height: 1200px;
    overflow: hidden;
  }
  .scene-photo {
    position: absolute;
    inset: 0;
    background:
      radial-gradient(ellipse 260px 360px at 960px 980px, var(--hay) 0%, rgba(169,119,61,0) 100%),
      linear-gradient(180deg, #b9c987 0%, var(--leaf-gold) 22%, #c7a25a 45%, #b77a4b 62%, var(--path-grey) 78%, #7e857e 100%);
  }
  .notice {
    position: absolute;
    left: 82px;
    top: 110px;
    width: 870px;
    height: 990px;
  }
  .notice svg { position: absolute; inset: 0; }
  .notice-content {
    position: absolute;
    inset: 0;
    text-align: center;
    color: var(--ink);
  }
  .title {
    font-family: "Rye", serif;
    font-weight: 400;
    line-height: 1;
    white-space: nowrap;
  }
  .title-main {
    position: absolute;
    left: 0; right: 0;
    top: 120px;
    font-size: 74px;
  }
  .title-sub {
    position: absolute;
    left: 0; right: 0;
    top: 212px;
    font-size: 56px;
  }
  .tagline {
    position: absolute;
    left: 0; right: 0;
    top: 308px;
    font-family: "Raleway", sans-serif;
    font-weight: 500;
    font-size: 27px;
    text-transform: uppercase;
  }
  .day {
    position: absolute;
    left: 0; right: 0;
    top: 398px;
    font-family: "Montserrat", sans-serif;
    font-weight: 700;
    font-size: 70px;
    line-height: 1;
  }
  .date {
    position: absolute;
    left: 0; right: 0;
    top: 480px;
    font-family: "Montserrat", sans-serif;
    font-weight: 600;
    font-size: 31px;
  }
  .time-row {
    position: absolute;
    left: 90px; right: 90px;
    top: 552px;
    display: flex;
    align-items: center;
    justify-content: center;
    gap: 16px;
  }
  .time-rule {
    flex: 1;
    height: 3px;
    background: var(--orange);
  }
  .time-badge {
    background: var(--orange);
    padding: 6px 44px;
    font-family: "Montserrat", sans-serif;
    font-weight: 700;
    font-size: 32px;
    color: var(--ink);
    white-space: nowrap;
  }
  .celebrate {
    position: absolute;
    left: 130px; right: 50px;
    top: 680px;
    font-family: "Rye", serif;
    font-size: 33px;
    line-height: 1.45;
    text-transform: uppercase;
    white-space: nowrap;
  }
  .tickets {
    position: absolute;
    left: 130px; right: 50px;
    top: 880px;
    font-family: "Raleway", sans-serif;
    font-weight: 500;
    font-size: 27px;
    line-height: 1.3;
  }
  .tickets strong { font-weight: 700; }
</style>
</head>
<body>
<main class="poster">
  <div class="scene-photo" role="img" aria-label="Photograph of an autumn woodland path with golden trees, fallen leaves on the pavement and round hay bales at the right"></div>

  <section class="notice">
    <svg width="870" height="990" viewBox="0 0 870 990" aria-hidden="true">
      <rect x="8" y="8" width="854" height="974" rx="14" fill="var(--panel)" stroke="var(--orange)" stroke-width="10"/>
    </svg>
    <div class="notice-content">
      <h1 class="title title-main">Brass Lantern</h1>
      <h2 class="title title-sub">Pebble Lane Grove</h2>
      <p class="tagline">Maple and Wren Unite</p>
      <p class="day">SATURDAY</p>
      <p class="date">OCTOBER 19th 2019</p>
      <div class="time-row">
        <span class="time-rule"></span>
        <span class="time-badge">12:00-4:00pm</span>
        <span class="time-rule"></span>
      </div>
      <p class="celebrate">Celebrate M&amp;W with<br>great food, music,<br>entertainment,<br>and fun!</p>
      <p class="tickets">Tickets will be available for sale<br><strong>at Drop off and Pick up</strong></p>
    </div>
  </section>
</main>
</body>
</html>
```